Interior Stylist business card design needed

I need a business card for my new company in Sydney called "Pip Dunstane Designs". The business offers an interior styling and colour consultancy. My clients are generally not very design savvy (hence why they use me) and can range from being quite conservative to really wanting something "out there". They can be looking for a budget makeover or something more expensive / substantial. I'd like my business card design to be stylish (but not overly formal). I certainly don't want it to be conservative. I'd like it to stand out a bit! I don't really have any aversion to particular colours and I don't have a logo as such - my business name is really all I have.

Target Market(s)

As above - home owners, ranging from conservative to modern

Industry/Entity Type

Conservative

Contact Information for Business Card

Pip Dunstane Designs
Colour consultancy and interior styling
ph: 0417 382 605
email: pipdunstane@harvolink.net.au

Requirements
Should not have
• Old fashioned writing or motifs. No Times Roman font!!

```html
<!DOCTYPE html>
<html lang="en">
<head>
<meta charset="utf-8">
<title>Pip Dunstane Designs – Business Card</title>
<link rel="stylesheet" href="https://fonts.googleapis.com/css2?family=Caveat:wght@400;500&display=swap">
<style>
  :root {
    --stripe-light: #a4232c;
    --stripe-dark: #8c232a;
    --field-red: #942429;
    --ink-white: #ffffff;
  }
  html, body {
    margin: 0;
    padding: 0;
    width: 1200px;
    height: 741px;
    overflow: hidden;
    background: var(--field-red);
  }
  .card {
    display: block;
    width: 1200px;
    height: 741px;
  }
  .card-text {
    font-family: "Caveat", cursive;
    fill: var(--ink-white);
  }
  .name-heading { font-size: 70px; font-weight: 500; }
  .service-line { font-size: 48px; font-weight: 400; }
  .contact-line { font-size: 44px; font-weight: 400; }
  .brand-name { font-size: 48px; font-weight: 500; }
  .stripe-light { fill: var(--stripe-light); }
  .stripe-dark { fill: var(--stripe-dark); }
  .field { fill: var(--field-red); }
</style>
</head>
<body>
<svg class="card" viewBox="0 0 1200 741" xmlns="http://www.w3.org/2000/svg" aria-label="Pip Dunstane Designs business card">
  <g class="background-stripes">
    <rect class="stripe-light" x="0" y="0" width="119" height="741"/>
    <rect class="stripe-dark" x="119" y="0" width="86" height="741"/>
    <rect class="stripe-light" x="205" y="0" width="85" height="741"/>
    <rect class="stripe-dark" x="290" y="0" width="83" height="741"/>
    <rect class="stripe-light" x="373" y="0" width="86" height="741"/>
    <rect class="stripe-dark" x="459" y="0" width="82" height="741"/>
    <rect class="stripe-light" x="541" y="0" width="84" height="741"/>
    <rect class="field" x="625" y="0" width="575" height="741"/>
  </g>

  <g class="brand-name-block">
    <text class="card-text brand-name" x="268" y="330" text-anchor="middle">Pip Dunstane Designs</text>
  </g>

  <g class="contact-block">
    <text class="card-text name-heading" x="643" y="290" textLength="454" lengthAdjust="spacingAndGlyphs">Pip Dunstane Designs</text>
    <text class="card-text service-line" x="641" y="422">Colour Consultancy</text>
    <text class="card-text service-line" x="641" y="495">&amp; Interior Styling</text>
    <text class="card-text contact-line" x="641" y="607">Ph: 0417 382 605</text>
    <text class="card-text contact-line" x="641" y="681" textLength="500" lengthAdjust="spacingAndGlyphs">Email: pipdunstane@harvolink.net.au</text>
  </g>
</svg>
</body>
</html>
```